Billboard design for a new container self storage

I’m after a sign designing for a new container storage opening. located in the heart of Scunthorpe. Open 24/7. Brand new containers. On site security. Best prices guaranteed

Open 24/7
Safe secure self storage
Best prices Guaranteed
Site address
Tarbury Row
Scunthorpe
ZX48 2QT
Also include next left and an arrow
Dark green/ grey and fluorescent lime green

Contact - info@marshvaleunits.co.uk
07946201583

Website colours attached

Requirements
Must have
• Instagram logo @Marshvaleselfstorage

```html
<!DOCTYPE html>
<html lang="en">
<head>
<meta charset="utf-8">
<title>Marshvale Secure Self Storage – Billboard</title>
<link rel="stylesheet" href="https://fonts.googleapis.com/css2?family=Bebas+Neue&family=Montserrat:ital,wght@0,500;0,600;0,700;0,800;1,800&display=swap">
<style>
  :root {
    --page-bg: #a9a9a9;
    --lime: #dcff1e;
    --deep-green: #24501f;
    --container-green: #1f6a2a;
    --container-dark: #144a1c;
    --ground-dark: #1b1b1b;
    --sky: #7f99a4;
    --white: #ffffff;
    --ink: #111511;
  }
  * { box-sizing: border-box; margin: 0; padding: 0; }
  html, body {
    width: 1052px; height: 1200px; overflow: hidden;
    background: var(--page-bg);
    font-family: "Montserrat", sans-serif;
  }
  .billboard {
    position: absolute; left: 26px; top: 350px;
    width: 1000px; height: 500px; overflow: hidden;
    box-shadow: 10px 10px 18px rgba(0,0,0,.45);
  }
  .backdrop-photo {
    position: absolute; inset: 0;
    background: linear-gradient(180deg, var(--sky) 0%, #5b6b6e 55%, #3a3a3a 80%, var(--ground-dark) 100%);
  }
  .container-photo {
    position: absolute; left: 58px; top: 17px; width: 880px; height: 360px;
    background: linear-gradient(90deg, var(--container-dark) 0%, var(--container-green) 30%, #237a30 60%, var(--container-dark) 100%);
  }
  .open-pill {
    position: absolute; left: 104px; top: 76px; width: 218px; height: 53px;
    border: 3px solid var(--white); border-radius: 27px; overflow: hidden;
    display: flex; align-items: center;
    background: var(--lime);
  }
  .open-pill .hours {
    background: var(--deep-green); color: var(--white);
    height: 100%; width: 96px; display: flex; align-items: center; padding-left: 14px;
    font-weight: 800; font-size: 25px; border-radius: 0 24px 24px 0;
  }
  .open-pill .clock { position: absolute; left: 80px; top: 6px; }
  .open-pill .state {
    margin-left: 26px; font-weight: 800; font-style: italic; font-size: 25px; color: var(--ink);
  }
  .brand {
    position: absolute; left: 300px; top: 116px; width: 400px; text-align: center; color: var(--white);
  }
  .brand-name {
    display: inline-flex; align-items: center; gap: 12px;
    font-weight: 600; font-size: 44px; letter-spacing: 2px; line-height: 1;
  }
  .brand-name .mark { width: 16px; height: 16px; background: var(--white); }
  .brand-tagline { margin-top: 6px; font-size: 11px; font-weight: 500; letter-spacing: 3px; }
  .feature-icon { position: absolute; }
  .feature-text {
    position: absolute; font-weight: 800; font-size: 29px; line-height: 35px; letter-spacing: .3px;
  }
  .feature-text .accent { color: var(--lime); }
  .feature-text .plain { color: var(--white); }
  .divider { position: absolute; left: 505px; top: 212px; width: 3px; height: 76px; background: var(--white); }
  .location-line {
    position: absolute; left: 0; top: 308px; width: 1000px; text-align: center;
    color: var(--white); font-weight: 700; font-size: 21px;
  }
  .location-line .accent { color: var(--lime); }
  .direction-arrow { position: absolute; left: 30px; top: 346px; }
  .address-band {
    position: absolute; left: 88px; top: 366px; width: 440px; height: 64px; background: var(--white);
    display: flex; align-items: center; padding-left: 12px; gap: 8px;
    font-family: "Bebas Neue", sans-serif; font-size: 27px; color: var(--ink); letter-spacing: 0;
    white-space: nowrap;
  }
  .phone-band {
    position: absolute; left: 510px; top: 366px; width: 432px; height: 64px; background: var(--lime);
    display: flex; align-items: center; padding-left: 41px;
    font-weight: 800; font-size: 47px; color: var(--ink); letter-spacing: 1px;
  }
  .phone-badge { position: absolute; left: 486px; top: 372px; }
  .contact-row {
    position: absolute; left: 0; top: 446px; width: 1000px;
    display: flex; justify-content: center; align-items: center; gap: 14px;
    color: var(--white); font-weight: 600; font-size: 21px;
  }
  .contact-row .accent { color: var(--lime); }
  .contact-row .sep { width: 1px; height: 26px; background: #bbb; }
  .contact-item { display: flex; align-items: center; gap: 10px; }
  .social-square { width: 24px; height: 24px; border: 2.5px solid var(--white); border-radius: 6px; }
</style>
</head>
<body>
<main class="billboard">
  <div class="backdrop-photo" role="img" aria-label="Sky and yard ground behind the container"></div>
  <div class="container-photo" role="img" aria-label="Photo of a green corrugated shipping container"></div>

  <div class="open-pill">
    <span class="hours">24/7</span>
    <svg class="clock" width="36" height="36" viewBox="0 0 36 36">
      <circle cx="18" cy="18" r="16" fill="var(--deep-green)" stroke="var(--white)" stroke-width="2"/>
      <circle cx="18" cy="18" r="11" fill="#e8f0d8"/>
      <path d="M18 11v7l5 3" stroke="var(--ink)" stroke-width="2" fill="none" stroke-linecap="round"/>
    </svg>
    <span class="state">OPEN</span>
  </div>

  <div class="brand">
    <div class="brand-name"><span class="mark"></span>MARSHVALE</div>
    <div class="brand-tagline">SECURE SELF STORAGE</div>
  </div>

  <svg class="feature-icon" style="left:130px;top:205px" width="76" height="86" viewBox="0 0 76 86">
    <polygon points="38,3 73,23 73,63 38,83 3,63 3,23" fill="#3f7a3a" stroke="#d8e6d2" stroke-width="4"/>
    <rect x="20" y="34" width="36" height="22" fill="none" stroke="var(--white)" stroke-width="2.5"/>
    <path d="M27 38v14M33 38v14M39 38v14M45 38v14M30 34l8-8 8 8" stroke="var(--white)" stroke-width="2" fill="none"/>
  </svg>
  <div class="feature-text" style="left:233px;top:212px">
    <div class="accent">SAFE SECURE</div>
    <div class="plain">SELF STORAGE</div>
  </div>

  <div class="divider"></div>

  <svg class="feature-icon" style="left:536px;top:203px" width="76" height="86" viewBox="0 0 76 86">
    <polygon points="38,3 73,23 73,63 38,83 3,63 3,23" fill="#3f7a3a" stroke="#d8e6d2" stroke-width="4"/>
    <circle cx="38" cy="36" r="13" fill="none" stroke="var(--white)" stroke-width="2.5"/>
    <path d="M30 47l-7 14 6-1 3 5 6-13M46 47l7 14-6-1-3 5-6-13" stroke="var(--white)" stroke-width="2.5" fill="none"/>
    <text x="38" y="42" text-anchor="middle" font-family="Montserrat, sans-serif" font-weight="700" font-size="16" fill="var(--white)">$</text>
  </svg>
  <div class="feature-text" style="left:638px;top:210px">
    <div class="accent">BEST PRICES</div>
    <div class="plain">GUARANTEED</div>
  </div>

  <p class="location-line">Secure self storage container facility <span class="accent">in Scunthorpe,</span> Lincolnshire</p>

  <svg class="direction-arrow" width="62" height="104" viewBox="0 0 62 104">
    <polygon points="0,52 60,0 60,104" fill="var(--white)"/>
  </svg>
  <div class="address-band">
    <svg width="20" height="26" viewBox="0 0 20 26"><path d="M10 1a9 9 0 0 0-9 9c0 7 9 15 9 15s9-8 9-15a9 9 0 0 0-9-9z" fill="#3f9a2f"/><circle cx="10" cy="10" r="3.5" fill="var(--white)"/></svg>
    <span>TARBURY ROW SCUNTHORPE ZX48 2QT</span>
  </div>
  <div class="phone-band">07946 201583</div>
  <svg class="phone-badge" width="52" height="52" viewBox="0 0 52 52">
    <circle cx="26" cy="26" r="25" fill="var(--deep-green)"/>
    <circle cx="26" cy="26" r="19" fill="none" stroke="var(--lime)" stroke-width="2"/>
    <path d="M18 16c2-1 4 3 4 4s-2 2-2 3 4 7 6 8 2-1 3-2 5 2 4 4-3 3-5 3c-6-1-13-9-13-15 0-2 1-4 3-5z" fill="var(--lime)"/>
  </svg>

  <div class="contact-row">
    <div class="contact-item">
      <svg width="26" height="18" viewBox="0 0 26 18"><rect x="1" y="1" width="24" height="16" fill="none" stroke="var(--white)" stroke-width="2"/><path d="M1 1l12 9 12-9M1 17l9-8M25 17l-9-8" stroke="var(--white)" stroke-width="2" fill="none"/></svg>
      <span>info@<span class="accent">marshvaleunits</span>.co.uk</span>
    </div>
    <span class="sep"></span>
    <div class="contact-item">
      <span class="social-square"></span>
      <span>@<span class="accent">Marshvaleselfstorage</span></span>
    </div>
  </div>
</main>
</body>
</html>
```